property investment and development company needs a website

we need a website that looks professional and portrays trust for people looking to us to buy their house or investors looking to invest or joint venture with us.
We are based in the west midlands in the UK.
we deal mainly with residential housing, house to flats conversions, HMO's (houses in multiple ocupancy).
we require the website as a first point of contact with potential sellers, renters and investors so links or contact details that are easy to access or see would be good.
I have had logos designed by a plan hollow member and these can be used as guidance for the colour and style of the site.
Target Market(s)
joint venture investment partners, people looking to sell their house, people looking to rent from us.
Coding
Coded - Design and coding required
Number of Pages Required
3 page
Requirements
Must have
- project a professional appearance
- visable contact details

```html
<!DOCTYPE html>
<html lang="en">
<head>
<meta charset="utf-8">
<title>Harlow Homes – Property Development and Investment</title>
<link rel="stylesheet" href="https://fonts.googleapis.com/css2?family=Montserrat:wght@400;500;600;700;800&family=Libre+Baskerville:wght@700&display=swap">
<style>
:root{
  --navy:#1f2535;
  --navy-deep:#171c29;
  --gold:#c6a66a;
  --gold-light:#d9bf8c;
  --beige:#f3ede4;
  --ink:#2a2d35;
  --white:#ffffff;
  --field-line:#e3ddd2;
}
*{box-sizing:border-box;margin:0;padding:0}
html,body{width:1200px;height:4467px;overflow:hidden}
body{font-family:"Montserrat",Arial,sans-serif;color:var(--ink);background:var(--white);position:relative}
section,header,footer{position:absolute;left:0;width:1200px;overflow:hidden}
.abs{position:absolute}

/* header / hero */
.hero{top:0;height:700px;background:var(--navy)}
.hero-photo{position:absolute;inset:0;background:radial-gradient(ellipse at 72% 40%,#6f7c92 0%,#3d4860 30%,#222a3c 65%,#1a2030 100%)}
.brand{position:absolute;left:45px;top:46px;display:flex;align-items:center;gap:14px}
.brand-square{width:34px;height:34px;background:var(--gold)}
.brand-name{font-family:"Montserrat",Arial,sans-serif;font-weight:600;color:var(--white);font-size:22px;line-height:24px;letter-spacing:2px}
.main-nav{position:absolute;right:46px;top:74px;display:flex;gap:30px;font-size:15px;font-weight:500;letter-spacing:.5px}
.main-nav a{color:var(--white);text-decoration:none}
.main-nav a.current{color:var(--gold)}
.hero-title{position:absolute;left:0;width:1200px;top:300px;text-align:center;color:var(--white);font-weight:800;font-size:46px;line-height:56px;text-shadow:0 3px 8px rgba(0,0,0,.6)}
.slide-arrow{position:absolute;top:345px;width:52px;height:44px;background:#11141c}
.slide-arrow.prev{left:30px}.slide-arrow.next{right:30px}
.slide-arrow svg{position:absolute;left:18px;top:13px}
.hero-base{position:absolute;left:0;top:0}
.slide-dots{position:absolute;top:636px;left:540px;display:flex;gap:8px}
.slide-dots span{width:32px;height:4px;background:var(--gold)}
.slide-dots span.on{background:var(--white)}

/* services */
.services{top:700px;height:232px;background:var(--navy)}
.services-title{position:absolute;top:60px;width:1200px;text-align:center;color:var(--white);font-weight:700;font-size:22px;letter-spacing:.3px}
.services-title em{font-style:normal;color:var(--gold)}
.service{position:absolute;top:118px;display:flex;align-items:center;gap:16px;color:var(--white);font-size:17px;font-weight:500;line-height:22px}

/* section headings */
.section-heading{display:flex;align-items:center;gap:12px;font-weight:800;font-size:31px;color:var(--navy);letter-spacing:.5px}
.section-heading .mark{width:34px;height:34px;background:var(--gold)}
.section-heading .rule{width:3px;height:40px;background:var(--navy)}
.on-dark .section-heading{color:var(--white)}
.on-dark .section-heading .rule{background:var(--white)}

.btn{display:inline-block;background:var(--navy);color:var(--white);font-family:"Libre Baskerville",Georgia,serif;font-weight:700;font-size:17px;padding:12px 32px;border-radius:3px}

/* about */
.about{top:932px;height:453px;background:var(--beige)}
.about .section-heading{position:absolute;top:96px;left:0;width:1200px;justify-content:center}
.about-text{position:absolute;top:185px;left:110px;width:980px;text-align:center;font-size:17.5px;line-height:32px}
.about .btn{position:absolute;top:318px;left:512px}

/* invest */
.invest{top:1385px;height:555px;background:var(--white)}
.photo-ring{position:absolute;width:326px;height:326px;border-radius:50%;border:12px solid var(--gold);background:radial-gradient(circle at 50% 45%,#c9b09a 0%,#6e7f99 35%,#2b3550 75%)}
.invest .photo-ring{left:95px;top:45px}
.invest .section-heading{position:absolute;left:476px;top:96px}
.body-copy{font-size:17px;line-height:30px}
.invest .body-copy{position:absolute;left:476px;top:180px;width:640px}
.body-copy p+p{margin-top:28px}

/* portfolio */
.portfolio{top:1940px;height:760px;background:var(--white)}
.portfolio-bg{position:absolute;left:0;top:0}
.portfolio .section-heading{position:absolute;top:96px;left:0;width:1200px;justify-content:center}
.card{position:absolute;top:185px;width:450px;height:400px;background:var(--beige);border-bottom:4px solid #3b74c5}
.card.one{left:137px}.card.two{left:620px}
.card-photo{position:absolute;left:0;top:0;width:450px;height:262px}
.card.one .card-photo{background:linear-gradient(180deg,#5f7a45 0%,#8a6a4a 45%,#6d8a3c 75%,#b7aa8e 100%)}
.card.two .card-photo{background:linear-gradient(180deg,#8fb0d8 0%,#e9ecef 40%,#6f9a3e 70%,#7fae3f 100%)}
.card-corner{position:absolute;right:0;top:0}
.card-body{position:absolute;left:20px;top:280px;width:410px;font-size:16px;line-height:22px}
.card-body h3{font-size:16px;font-weight:600;letter-spacing:.3px}
.round-arrow{position:absolute;top:380px;width:26px;height:26px;border-radius:50%;background:#c8cbd2;border:3px solid #9aa0ab}
.round-arrow.prev{left:67px}.round-arrow.next{right:67px}

/* sell */
.sell{top:2700px;height:600px;background:var(--white)}
.sell .section-heading{position:absolute;left:95px;top:90px}
.sell .body-copy{position:absolute;left:95px;top:170px;width:640px}
.sell .btn{position:absolute;left:95px;top:462px}
.sell .photo-ring{left:780px;top:90px}

/* contact */
.contact{top:3300px;height:503px;background:var(--beige)}
.contact .section-heading{position:absolute;top:92px;left:0;width:1200px;justify-content:center}
.field{position:absolute;height:40px;background:var(--white);font-size:16px;color:#555;padding:9px 16px}
.field.message{height:80px}
.field .caret{position:absolute;right:16px;top:15px}
.contact .btn{position:absolute;left:516px;top:382px;padding:10px 56px;font-size:16px}

/* newsletter */
.newsletter{top:3803px;height:250px;background:var(--white)}
.newsletter-title{position:absolute;left:170px;top:74px;color:var(--gold);font-weight:800;font-size:30px;letter-spacing:.5px}
.signup{position:absolute;left:575px;top:70px;width:462px;height:50px;border-radius:25px;background:var(--white);border:2px solid #d6d6d6}
.signup span{position:absolute;left:22px;top:14px;font-size:15px;font-weight:500;color:#222}
.signup b{position:absolute;right:8px;top:7px;width:140px;height:32px;border-radius:16px;background:var(--gold);color:var(--white);font-size:15px;font-weight:700;text-align:center;line-height:32px}

/* footer */
.site-footer{top:4053px;height:360px;background:var(--white)}
.footer-brand{position:absolute;left:160px;top:96px;display:flex;align-items:center;gap:14px}
.footer-brand .brand-name{color:var(--navy)}
.footer-col{position:absolute;top:92px;font-size:13px;line-height:20px;font-weight:600;color:var(--ink)}
.footer-col h4{font-size:14px;font-weight:700;margin-bottom:22px;letter-spacing:.3px}
.contact-item{display:flex;gap:8px;margin-bottom:16px}
.contact-item svg{flex:none;margin-top:2px}
.social{display:flex;gap:6px}
.social span{width:22px;height:22px;border-radius:50%;border:2px solid var(--ink)}
.copyright{top:4413px;height:54px;background:var(--navy);color:var(--gold);font-size:12px;font-weight:600;text-align:center;line-height:54px;letter-spacing:.3px}
</style>
</head>
<body>

<header class="hero">
  <div class="hero-photo" role="img" aria-label="Photograph of open hands holding a small model house against a dark blue blurred background"></div>
  <div class="brand"><span class="brand-square"></span><span class="brand-name">HARLOW<br>HOMES</span></div>
  <nav class="main-nav">
    <a class="current">HOME</a><a>ABOUT US</a><a>INVEST</a><a>PORTFOLIO</a><a>SELL</a><a>NEWS</a><a>CONTACT</a>
  </nav>
  <h1 class="hero-title">THE LEADER IN PROPERTY<br>DEVELOPMENT AND INVESTMENT</h1>
  <div class="slide-arrow prev"><svg width="14" height="18" viewBox="0 0 14 18"><path d="M11 2 4 9l7 7" fill="none" stroke="#fff" stroke-width="3"/></svg></div>
  <div class="slide-arrow next"><svg width="14" height="18" viewBox="0 0 14 18"><path d="M3 2l7 7-7 7" fill="none" stroke="#fff" stroke-width="3"/></svg></div>
  <svg class="hero-base" width="1200" height="700" viewBox="0 0 1200 700">
    <polygon points="0,602 600,682 1200,602 1200,700 0,700" fill="#1f2535"/>
    <polyline points="0,600 600,680 1200,600" fill="none" stroke="#c6a66a" stroke-width="5"/>
  </svg>
  <div class="slide-dots"><span class="on"></span><span></span><span></span></div>
</header>

<section class="services">
  <h2 class="services-title">WHATEVER YOUR PROPERTY NEEDS, WE DELIVER <em>BESPOKE SERVICES</em> FOR OUR CLIENTS</h2>
  <div class="service" style="left:108px">
    <svg width="62" height="50" viewBox="0 0 62 50" fill="none" stroke="#c6a66a" stroke-width="3"><path d="M4 24 31 4l27 20"/><rect x="10" y="22" width="42" height="25"/><rect x="26" y="31" width="10" height="16"/><rect x="14" y="28" width="8" height="7"/><rect x="40" y="28" width="8" height="7"/></svg>
    <span>Residential Housing</span>
  </div>
  <div class="service" style="left:476px">
    <svg width="60" height="54" viewBox="0 0 60 54" fill="none" stroke="#c6a66a" stroke-width="3"><rect x="6" y="6" width="48" height="45"/><path d="M2 6h56"/><rect x="13" y="13" width="9" height="8"/><rect x="26" y="13" width="9" height="8"/><rect x="39" y="13" width="9" height="8"/><rect x="13" y="27" width="9" height="8"/><rect x="26" y="27" width="9" height="8"/><rect x="39" y="27" width="9" height="8"/><rect x="25" y="40" width="10" height="11"/></svg>
    <span>House to Flats Conversions</span>
  </div>
  <div class="service" style="left:845px">
    <svg width="64" height="56" viewBox="0 0 64 56" fill="none" stroke="#c6a66a" stroke-width="3"><path d="M4 16 32 4l28 12"/><rect x="8" y="16" width="48" height="37"/><rect x="14" y="22" width="8" height="7"/><rect x="28" y="22" width="8" height="7"/><rect x="42" y="22" width="8" height="7"/><rect x="14" y="34" width="8" height="7"/><rect x="42" y="34" width="8" height="7"/><rect x="28" y="36" width="8" height="17"/></svg>
    <span>HMO (Houses in<br>Multiple Occupancy</span>
  </div>
</section>

<section class="about">
  <h2 class="section-heading"><span class="mark"></span><span class="rule"></span>ABOUT US</h2>
  <p class="about-text">We are a property development and investment company that have our own portfolio and we are active investors who pride ourselves in expanding our business organically. We ensure that whatever your property needs are we are deliver bespoke services for our clients. For investors, sellers, landlords and tenants we bring knowledge to your next property decision, allowing you to make an informed decision.</p>
  <span class="btn">Learn More</span>
</section>

<section class="invest">
  <div class="photo-ring" role="img" aria-label="Photograph of a hand in a suit sleeve holding a small model house"></div>
  <h2 class="section-heading"><span class="mark"></span><span class="rule"></span>INVEST</h2>
  <div class="body-copy">
    <p>We have our own portfolio and we are active investors, so our finger is on the pulse and we are currently looking for residential development investments and commercial to residential conversions in cities or regional centres showing strong growth.</p>
    <p>Our experience in the industry enables us to make extremely quick and well-informed decisions. We follow the opportunities that are presented to us as well as sourcing opportunities ourselves. We are happy to work in partnership and within joint ventures and have a proven track record of establishing excellent relationships in these areas.</p>
  </div>
</section>

<section class="portfolio on-dark">
  <svg class="portfolio-bg" width="1200" height="760" viewBox="0 0 1200 760">
    <defs><linearGradient id="portfolioShade" x1="0" y1="0" x2="0" y2="1"><stop offset="0" stop-color="#2a3144"/><stop offset="1" stop-color="#1d2333"/></linearGradient></defs>
    <polygon points="0,0 1200,0 1200,640 600,720 0,640" fill="url(#portfolioShade)"/>
    <polygon points="0,640 600,720 1200,640 1200,656 600,758 0,656" fill="#c6a66a"/>
  </svg>
  <h2 class="section-heading"><span class="mark"></span><span class="rule"></span>PORTFOLIO</h2>
  <span class="round-arrow prev"></span>
  <span class="round-arrow next"></span>
  <article class="card one">
    <div class="card-photo" role="img" aria-label="Photograph of a large stone and timber house with a lawn and trees"></div>
    <svg class="card-corner" width="110" height="110" viewBox="0 0 110 110"><polygon points="0,0 110,0 110,110" fill="#fff"/><circle cx="84" cy="26" r="12" fill="none" stroke="#1f2535" stroke-width="2"/><path d="M80 30l8-8m-6 0h6v6" fill="none" stroke="#1f2535" stroke-width="2"/></svg>
    <div class="card-body"><h3>WILSHIRE RESIDENT</h3><p>Lorem ipsum dolor sit amet, consectetuer adipiscing elit, sed diam nonummy nibh euismod tincidunt ut laoreet dolore.</p></div>
  </article>
  <article class="card two">
    <div class="card-photo" role="img" aria-label="Photograph of a white modern house with a green lawn under a blue sky"></div>
    <svg class="card-corner" width="110" height="110" viewBox="0 0 110 110"><polygon points="0,0 110,0 110,110" fill="#fff"/><circle cx="84" cy="26" r="12" fill="none" stroke="#1f2535" stroke-width="2"/><path d="M80 30l8-8m-6 0h6v6" fill="none" stroke="#1f2535" stroke-width="2"/></svg>
    <div class="card-body"><h3>ADAM RESIDENT</h3><p>Lorem ipsum dolor sit amet, consectetuer adipiscing elit, sed diam nonummy nibh euismod tincidunt ut laoreet dolore.</p></div>
  </article>
</section>

<section class="sell">
  <h2 class="section-heading"><span class="mark"></span><span class="rule"></span>SELL</h2>
  <div class="body-copy">
    <p>We undertake the necessary market research to evaluate an option that works for all parties involved. We will help guide you to make an informed decision on how to gain the maximum realistic value.</p>
    <p>For those looking to achieve a fast and professional sale to experienced investors, we provide an approach that has been proven to work for many others. If you would like to discuss a property you are looking to sell, then please contact us on 01632 960418</p>
  </div>
  <span class="btn">Learn More</span>
  <div class="photo-ring" role="img" aria-label="Photograph of a hand in a suit sleeve holding a small model house"></div>
</section>

<section class="contact">
  <h2 class="section-heading"><span class="mark"></span><span class="rule"></span>CONTACT US</h2>
  <div class="field" style="left:164px;top:190px;width:430px">First Name</div>
  <div class="field" style="left:606px;top:190px;width:430px">Last Name</div>
  <div class="field" style="left:164px;top:243px;width:430px">Email</div>
  <div class="field" style="left:606px;top:243px;width:430px">Interested In<svg class="caret" width="18" height="10" viewBox="0 0 18 10"><polygon points="0,0 18,0 9,10" fill="#444"/></svg></div>
  <div class="field message" style="left:164px;top:296px;width:872px">Message</div>
  <span class="btn">Send</span>
</section>

<section class="newsletter">
  <svg class="abs" style="left:0;top:0" width="1200" height="250" viewBox="0 0 1200 250">
    <defs><linearGradient id="newsShade" x1="0" y1="0" x2="1" y2="0"><stop offset="0" stop-color="#2c3446"/><stop offset=".5" stop-color="#3a4356"/><stop offset="1" stop-color="#262d3e"/></linearGradient></defs>
    <polygon points="0,0 1200,0 1200,160 600,212 0,160" fill="url(#newsShade)"/>
    <polygon points="0,160 600,212 1200,160 1200,174 600,240 0,174" fill="#c6a66a"/>
  </svg>
  <h2 class="newsletter-title">JOIN OUR NEWSLETTER</h2>
  <div class="signup"><span>Enter email address</span><b>SIGN UP</b></div>
</section>

<footer class="site-footer">
  <div class="footer-brand"><span class="brand-square"></span><span class="brand-name">HARLOW<br>HOMES</span></div>
  <div class="footer-col" style="left:447px">
    <h4>QUICK LINKS</h4>
    <div>Home</div><div>About Us</div><div>Invest</div><div>Portfolio</div><div>Sell</div><div>Contact</div>
  </div>
  <div class="footer-col" style="left:628px">
    <h4>CONTACT</h4>
    <div class="contact-item"><svg width="16" height="16" viewBox="0 0 16 16"><circle cx="8" cy="8" r="7" fill="none" stroke="#2a2d35" stroke-width="1.6"/><path d="M8 4a2.6 2.6 0 0 1 2.6 2.6C10.6 9 8 12 8 12S5.4 9 5.4 6.6A2.6 2.6 0 0 1 8 4z" fill="#2a2d35"/></svg><span>Harlow Homes &amp; Development Ltd<br>12 Fernley Road, Ashcombe,<br>Worcestershire, WR9 1AB</span></div>
    <div class="contact-item"><svg width="16" height="16" viewBox="0 0 16 16"><path d="M3 1.5 6 1l1.5 3.5-2 1.5a8 8 0 0 0 4.5 4.5l1.5-2L15 10l-.5 3c-6.5.8-12.3-5-11.5-11.5z" fill="none" stroke="#2a2d35" stroke-width="1.6"/></svg><span>Phone 01632 960418<br>Mobile 07700 900245</span></div>
    <div class="contact-item"><svg width="16" height="16" viewBox="0 0 16 16"><circle cx="8" cy="8" r="7" fill="none" stroke="#2a2d35" stroke-width="1.6"/><rect x="4" y="5.5" width="8" height="5.5" fill="none" stroke="#2a2d35" stroke-width="1.3"/><path d="M4 5.5l4 3 4-3" fill="none" stroke="#2a2d35" stroke-width="1.3"/></svg><span>info@harlowhomes.co.uk</span></div>
  </div>
  <div class="footer-col" style="left:947px">
    <h4>FOLLOW US</h4>
    <div class="social"><span></span><span></span><span></span></div>
  </div>
</footer>

<footer class="copyright">COPYRIGHT © 2019 HARLOW HOMES &amp; DEVELOPMENTS LTD. ALL RIGHTS RESERVED.</footer>

</body>
</html>
```